Wine business stationary
Italian fine wines
Wine business stationary -
Simple
Elena Park
online business - no physical address
elena@casalumbra.com.hk
www.casalumbra.com.hk
- Logo - Name - website

```html
<!DOCTYPE html>
<html lang="en">
<head>
<meta charset="utf-8">
<title>Casa Lumbra – Business Card</title>
<link rel="stylesheet" href="https://fonts.googleapis.com/css2?family=Open+Sans:wght@400;600&display=swap">
<style>
  :root {
    --backdrop: #ece8e2;
    --card-white: #ffffff;
    --card-wine: #6b2a1b;
    --mark-taupe: #a3958c;
    --ink-wine: #7a3624;
    --ink-grey: #6e6560;
    --cream: #f3ebe3;
  }
  * { margin: 0; padding: 0; box-sizing: border-box; }
  html, body {
    width: 1200px;
    height: 799px;
    overflow: hidden;
  }
  body {
    background: var(--backdrop);
    font-family: "Open Sans", Arial, sans-serif;
    position: relative;
  }
  .card {
    position: absolute;
    top: 245px;
    width: 520px;
    height: 310px;
    border-radius: 16px;
    box-shadow: 0 6px 18px rgba(0,0,0,0.12);
  }
  .card--front {
    left: 50px;
    background: var(--card-white);
  }
  .card--back {
    left: 630px;
    background: var(--card-wine);
    display: flex;
    flex-direction: column;
    align-items: center;
    justify-content: center;
    gap: 18px;
  }
  .brand-dot {
    width: 70px;
    height: 70px;
    border-radius: 50%;
    background: var(--mark-taupe);
  }
  .card--back .brand-dot { background: var(--cream); width: 92px; height: 92px; }
  .brand-name {
    font-weight: 600;
    color: var(--mark-taupe);
    letter-spacing: 0.04em;
    white-space: nowrap;
  }
  .card--back .brand-name { color: var(--cream); font-size: 46px; }
  .front-brand {
    position: absolute;
    left: 34px;
    top: 92px;
    display: flex;
    flex-direction: column;
    align-items: center;
    gap: 14px;
  }
  .front-brand .brand-name { font-size: 32px; }
  .corner-brand {
    position: absolute;
    right: 30px;
    top: 26px;
    display: flex;
    align-items: center;
    gap: 6px;
  }
  .corner-brand .brand-dot { width: 18px; height: 18px; background: var(--ink-wine); }
  .corner-brand .brand-name { font-size: 13px; color: var(--ink-wine); }
  .contact {
    position: absolute;
    left: 292px;
    top: 156px;
  }
  .contact__name {
    font-size: 19px;
    font-weight: 600;
    color: var(--ink-wine);
    margin-bottom: 14px;
  }
  .contact__list {
    list-style: none;
    font-size: 10.5px;
    line-height: 1.55;
    color: var(--ink-grey);
  }
  .contact__label {
    display: inline-block;
    width: 40px;
    font-weight: 600;
    color: var(--ink-wine);
  }
</style>
</head>
<body>
  <section class="card card--front" aria-label="Business card front">
    <div class="corner-brand">
      <span class="brand-dot"></span>
      <span class="brand-name">Casa Lumbra</span>
    </div>
    <div class="front-brand">
      <span class="brand-dot"></span>
      <span class="brand-name">Casa Lumbra</span>
    </div>
    <div class="contact">
      <p class="contact__name">Elena Park</p>
      <ul class="contact__list">
        <li><span class="contact__label">Phone:</span>+852 5550 1234</li>
        <li><span class="contact__label">Email:</span>elena@casalumbra.com.hk</li>
        <li><span class="contact__label">Web:</span>www.casalumbra.com.hk</li>
      </ul>
    </div>
  </section>

  <section class="card card--back" aria-label="Business card back">
    <span class="brand-dot"></span>
    <span class="brand-name">Casa Lumbra</span>
  </section>
</body>
</html>
```